Stationery Design Project

I would like professional stationery that will be branded with our logo.

also, I have application- multipage that I would like to brand. I will attach an example of one of the pages.

Perhaps- this could be the same design, but due to spacing, it may be best to do slight variations.

Target Market(s)

The audience is our donors and supporters who have a heart for the disenfranchised. They are mostly professional and often have significant wealth. They do their work with excellence and I want an image that makes them feel confident we know what we are doing. this is why i tend to say i want a professional look. Also, I want the feel to be uplifting, something that is somewhat artistic and classy.

Industry/Entity Type

It Professional

Font styles to use
Serif

Requirements
Must have
• Generally, simple but I do want a stylized look...

512-684-2730
www.brightmorrowfund.org
PO Box 384927 Dallas, TX 75211
admin@brightmorrowfund.org
Nice to have
• i like to use the colors in our logo
Should not have
• hearts and country look

```html
<!DOCTYPE html>
<html lang="en">
<head>
<meta charset="utf-8">
<title>Bright Morrow Fund – Business Cards</title>
<link rel="stylesheet" href="https://fonts.googleapis.com/css2?family=Cormorant+Garamond:ital,wght@0,500;1,500&family=Questrial&display=swap">
<style>
  :root {
    --backdrop: #2b2b2b;
    --card-dark: #3a3a3c;
    --card-light: #ffffff;
    --ink: #555555;
    --ink-dark: #333333;
    --brand-blue: #1f6fb8;
    --sky-blue: #2ea3e0;
    --silver: #d9d9d9;
    --rule: #cfcfcf;
  }
  * { margin: 0; padding: 0; box-sizing: border-box; }
  html, body {
    width: 1200px; height: 900px; overflow: hidden;
    background: var(--backdrop);
  }
  .stage {
    width: 1200px; height: 900px;
    display: flex; flex-direction: column; align-items: center; justify-content: center;
    gap: 60px;
  }
  .card {
    width: 560px; height: 320px; position: relative;
    box-shadow: 0 10px 30px rgba(0,0,0,.45);
  }
  .card--back { background: var(--card-dark); }
  .card--front { background: var(--card-light); }

  .brand { position: absolute; display: flex; align-items: center; gap: 12px; }
  .brand__dot {
    width: 46px; height: 46px; border-radius: 50%;
    background: var(--sky-blue); flex: none;
  }
  .brand__text { display: flex; flex-direction: column; }
  .brand__name {
    font-family: "Cormorant Garamond", serif; font-weight: 500;
    font-size: 22px; letter-spacing: 1.2px; text-transform: uppercase; line-height: 1;
    white-space: nowrap;
  }
  .brand__tagline {
    font-family: "Cormorant Garamond", serif; font-style: italic; font-weight: 500;
    font-size: 12px; align-self: flex-end; margin-top: 3px; white-space: nowrap;
  }
  .card--back .brand { left: 50%; top: 50%; transform: translate(-50%, -50%); }
  .card--back .brand__name, .card--back .brand__tagline { color: var(--silver); }

  .card--front .brand { left: 24px; top: 96px; }
  .card--front .brand__name, .card--front .brand__tagline { color: var(--ink); }

  .person {
    position: absolute; left: 372px; top: 92px;
    padding-left: 14px; border-left: 1px solid var(--rule);
    font-family: "Questrial", sans-serif; white-space: nowrap;
  }
  .person__name { color: var(--brand-blue); font-size: 15px; font-weight: 700; letter-spacing: .4px; text-transform: uppercase; }
  .person__role { color: var(--ink-dark); font-size: 12px; margin-top: 4px; }

  .contact {
    position: absolute; right: 28px; bottom: 30px; text-align: right;
    font-family: "Questrial", sans-serif; font-style: normal;
    font-size: 12px; line-height: 1.65; color: var(--ink); white-space: nowrap;
  }
  .contact__label { color: var(--brand-blue); font-weight: 700; }
</style>
</head>
<body>
<main class="stage">
  <section class="card card--back" aria-label="Card back">
    <div class="brand">
      <span class="brand__dot"></span>
      <div class="brand__text">
        <span class="brand__name">Bright Morrow Fund</span>
        <span class="brand__tagline">Where brighter days begin</span>
      </div>
    </div>
  </section>

  <section class="card card--front" aria-label="Card front">
    <div class="brand">
      <span class="brand__dot"></span>
      <div class="brand__text">
        <span class="brand__name">Bright Morrow Fund</span>
        <span class="brand__tagline">Where brighter days begin</span>
      </div>
    </div>

    <div class="person">
      <p class="person__name">Daniel Hartwell</p>
      <p class="person__role">Manager</p>
    </div>

    <address class="contact">
      <p>PO Box 384927 Dallas, TX 75211</p>
      <p><span class="contact__label">Tel:</span> 512-684-2730 · <span class="contact__label">Fax:</span> 512-684-2731</p>
      <p><span class="contact__label">Web:</span> www.brightmorrowfund.org · <span class="contact__label">Email:</span> admin@brightmorrowfund.org</p>
    </address>
  </section>
</main>
</body>
</html>
```